Bold Plum

I am starting a sharpening service for knives, scissors, and garden tools. It's a sole proprietorship, so it's a small business. The business name is "Bolt Plum." A one or two-page website is fine. Ember Guild has created a logo for me. There should be pictures of the things I sharpen. There will also be a price list for sharpened items. My address is: 18392 Calloway Lane, Marlow Springs, CA 91307. Phone number is 661-555-0172

```html
<!DOCTYPE html>
<html lang="en">
<head>
<meta charset="utf-8">
<title>Bolt Plum — Precision Sharpening</title>
<link rel="stylesheet" href="https://fonts.googleapis.com/css2?family=Michroma&family=Poppins:wght@400;500;600;700&display=swap">
<style>
:root{
  --ink:#0b0b0b;
  --panel:#1b1b1b;
  --panel-dark:#0e0e0e;
  --white:#ffffff;
  --soft:#d9d9d9;
  --muted:#bdbdbd;
  --gold:#d9a63a;
  --heading:'Michroma',sans-serif;
  --body:'Poppins',sans-serif;
}
*{margin:0;padding:0;box-sizing:border-box}
html,body{width:1200px;height:4823px;overflow:hidden}
body{background:var(--ink);color:var(--white);font-family:var(--body);position:relative}
.abs{position:absolute}
.h2{font-family:var(--heading);font-size:28px;letter-spacing:.5px;text-transform:uppercase;font-weight:400;white-space:nowrap;-webkit-text-stroke:.6px currentColor}
.center{left:0;width:1200px;text-align:center}
.rule{height:5px;width:82px;background:var(--white)}
.lead{font-size:13px;line-height:26px;color:var(--soft);text-align:center}
.btn{display:flex;align-items:center;justify-content:center;font-size:12px;font-weight:600;text-transform:uppercase;letter-spacing:.3px}
.btn-white{background:var(--white);color:var(--ink)}
.btn-ghost{border:2px solid var(--white);color:var(--white)}
.btn-dark{background:var(--ink);color:var(--white)}
.round{border-radius:50%;display:flex;align-items:center;justify-content:center}
.brand{font-family:var(--heading);font-size:19px;line-height:24px;color:var(--white);display:flex;align-items:center;gap:10px;white-space:nowrap}
.brand-mark{width:22px;height:22px;border-radius:50%;background:var(--white);flex:none}

/* header */
.site-header{top:0;left:0;width:1200px;height:109px;background:var(--panel)}
.header-call{left:951px;top:0;width:249px;height:109px;background:var(--panel-dark)}
.nav a{color:var(--white);text-decoration:none;font-size:13px;font-weight:500;text-transform:uppercase;position:absolute;top:46px}
.call-label{font-size:11px;color:var(--soft);text-transform:uppercase}
.call-number{font-size:18px;font-weight:700}

/* hero */
.hero{top:109px;left:0;width:1200px;height:662px;background:
 radial-gradient(ellipse 420px 300px at 870px 230px,#4a2a24 0%,#2a1a16 45%,transparent 80%),
 radial-gradient(ellipse 360px 140px at 520px 580px,#2c2219 0%,transparent 80%),
 linear-gradient(90deg,#080808 0%,#141110 60%,#1c1614 100%)}
.hero-title{font-family:var(--heading);font-size:31px;line-height:46px;text-transform:uppercase;font-weight:400;white-space:nowrap;-webkit-text-stroke:.6px currentColor}
.hero-text{font-size:15px;line-height:29px;color:var(--soft)}

/* services */
.services{top:771px;left:0;width:1200px;height:721px;background:radial-gradient(ellipse 700px 500px at 600px 300px,#151515,#070707)}
.service-icon{width:100px;height:100px;background:#141414;box-shadow:0 0 0 1px #2a2a2a}
.service-icon.active{background:var(--white)}
.service-name{font-size:15px;font-weight:600;text-transform:uppercase;text-align:center;width:240px}
.service-text{font-size:13px;line-height:26px;color:var(--soft);text-align:center;width:200px}

/* why */
.why{top:1492px;left:0;width:1200px;height:655px;background:linear-gradient(90deg,#121212,#1b1918 50%,#111)}
.why-photo{width:442px;height:442px;border-radius:50%;background:radial-gradient(circle at 45% 40%,#6b5a4d,#3a2f28 55%,#1a1614)}
.why-text{font-size:13px;line-height:26px;color:var(--soft);width:440px}
.checks li{list-style:none;position:absolute;left:0;font-size:14px;display:flex;align-items:center;gap:12px;white-space:nowrap}
.tick{width:13px;height:13px;border-radius:50%;background:var(--white);display:flex;align-items:center;justify-content:center}

/* pricing */
.pricing{top:2147px;left:0;width:1200px;height:712px;background:#050505}
.price-card{top:2443px;width:260px;height:292px;border:1px solid #3a3a3a;background:#151515}
.price-photo{width:100%;height:230px}
.price-bar{height:62px;display:flex;align-items:center;justify-content:space-between;padding:0 30px;font-size:13px;font-weight:500;text-transform:uppercase}
.price-bar span:last-child{color:var(--gold)}

/* how */
.how{top:2859px;left:0;width:1200px;height:657px;background:radial-gradient(ellipse 700px 400px at 600px 300px,#1e1e1e,#0c0c0c)}
.step-icon{width:138px;height:138px;background:var(--white)}
.step-name{font-size:15px;font-weight:600;text-transform:uppercase;text-align:center;width:300px;line-height:26px}

/* connect */
.connect{top:3516px;left:0;width:1200px;height:653px;background:linear-gradient(180deg,#0d0d0d,#121212)}
.c-icon{width:52px;height:52px;background:var(--white)}
.c-title{font-size:18px;font-weight:600;text-transform:uppercase;white-space:nowrap}
.c-text{font-size:13px;line-height:26px;color:var(--soft);white-space:nowrap}
.map{left:599px;top:3635px;width:457px;height:422px;background:linear-gradient(135deg,#d6d6d6,#c7c7c7)}

/* cta */
.cta{left:116px;top:4169px;width:968px;height:287px;background:linear-gradient(90deg,#f1f1f1,#e2e2e2)}
.cta-title{font-family:var(--heading);font-size:29px;color:var(--ink);text-transform:uppercase;font-weight:400;-webkit-text-stroke:.6px currentColor}
.cta-text{font-size:17px;color:#333}

/* footer */
.footer-nav a{color:var(--white);text-decoration:none;font-size:13px;font-weight:500;text-transform:uppercase;position:absolute;top:4544px}
.copy{font-size:11px;color:var(--soft)}
</style>
</head>
<body>

<header class="abs site-header">
  <div class="abs brand" style="left:101px;top:42px"><span class="brand-mark"></span>BOLT PLUM</div>
  <nav class="nav">
    <a href="#" style="left:350px">Home</a>
    <a href="#" style="left:417px">Services</a>
    <a href="#" style="left:513px">Pricing</a>
    <a href="#" style="left:600px">How it works</a>
  </nav>
  <div class="abs btn btn-white" style="left:749px;top:34px;width:137px;height:43px">Contact us</div>
  <div class="abs header-call"></div>
  <div class="abs round" style="left:922px;top:27px;width:54px;height:54px;background:var(--white)">
    <svg width="22" height="22" viewBox="0 0 24 24"><path fill="#111" d="M6.6 10.8a15 15 0 0 0 6.6 6.6l2.2-2.2c.3-.3.7-.4 1-.2 1.1.4 2.3.6 3.6.6.6 0 1 .4 1 1V20c0 .6-.4 1-1 1A17 17 0 0 1 3 4c0-.6.4-1 1-1h3.5c.6 0 1 .4 1 1 0 1.3.2 2.5.6 3.6.1.3 0 .7-.2 1z"/></svg>
  </div>
  <div class="abs call-label" style="left:996px;top:30px">Call us now</div>
  <div class="abs call-number" style="left:996px;top:54px">661-555-0172</div>
</header>

<section class="abs hero" role="img" aria-label="Hands slicing meat with a sharp knife on a wooden board in a dark kitchen"></section>
<h1 class="abs hero-title" style="left:101px;top:258px">Precision sharpening.<br>Professional results.</h1>
<p class="abs hero-text" style="left:101px;top:375px;width:500px">Knives, scissors, and garden tools professionally sharpened to restore performance, safety, and precision. Local, reliable, and crafted with care.</p>
<div class="abs btn btn-white" style="left:101px;top:503px;width:137px;height:40px">Call now</div>
<div class="abs btn btn-ghost" style="left:255px;top:503px;width:136px;height:40px">View pricing</div>

<section class="abs services"></section>
<h2 class="abs h2 center" style="top:906px">Expert sharpening services</h2>
<div class="abs rule" style="left:559px;top:962px"></div>
<p class="abs lead" style="left:190px;top:996px;width:820px">Lorem ipsum dolor sit amet, consectetur adipiscing elit, sed do eiusmod tempor incididunt ut labore et dolore magna aliqua. Ut enim ad minim veniam, quis nostrud exercitation ullamco laboris nisi ut aliquip ex ea</p>

<div class="abs round service-icon" style="left:152px;top:1113px">
  <svg width="46" height="46" viewBox="0 0 48 48" fill="none" stroke="#fff" stroke-width="2"><path d="M38 8 14 32l4 4L40 12z"/><path d="M14 32l-6 8 4 1 6-5"/></svg>
</div>
<div class="abs round service-icon" style="left:414px;top:1113px">
  <svg width="46" height="46" viewBox="0 0 48 48" fill="none" stroke="#fff" stroke-width="2"><circle cx="12" cy="34" r="5"/><circle cx="20" cy="40" r="5"/><path d="M15 30 40 8M23 36 42 12"/></svg>
</div>
<div class="abs round service-icon active" style="left:676px;top:1113px">
  <svg width="46" height="46" viewBox="0 0 48 48" fill="none" stroke="#111" stroke-width="2"><path d="M16 6l8 18 8-18M24 24l-8 18M24 24l8 18"/><circle cx="24" cy="24" r="2"/></svg>
</div>
<div class="abs round service-icon" style="left:938px;top:1113px">
  <svg width="46" height="46" viewBox="0 0 48 48" fill="none" stroke="#fff" stroke-width="2"><path d="M40 8 14 34M12 30l6 6M8 40l6-6"/></svg>
</div>

<div class="abs service-name" style="left:82px;top:1238px">Kitchen knives</div>
<div class="abs service-name" style="left:344px;top:1238px">Scissors &amp; shears</div>
<div class="abs service-name" style="left:606px;top:1238px">Garden tools</div>
<div class="abs service-name" style="left:868px;top:1238px">Specialty blades</div>
<p class="abs service-text" style="left:102px;top:1275px">Lorem ipsum dolor sit amet, tempor incididunt ut labore e</p>
<p class="abs service-text" style="left:364px;top:1275px">Lorem ipsum dolor sit amet, tempor incididunt ut labore e</p>
<p class="abs service-text" style="left:626px;top:1275px">Lorem ipsum dolor sit amet, tempor incididunt ut labore e</p>
<p class="abs service-text" style="left:888px;top:1275px">Lorem ipsum dolor sit amet, tempor incididunt ut labore e</p>

<section class="abs why"></section>
<div class="abs why-photo" style="left:114px;top:1582px" role="img" aria-label="Hands sharpening a chef's knife on a whetstone"></div>
<h2 class="abs h2" style="left:663px;top:1638px">Why choose us</h2>
<div class="abs rule" style="left:663px;top:1694px"></div>
<p class="abs why-text" style="left:663px;top:1726px">Lorem ipsum dolor sit amet, consectetur adipiscing elit, sed do eiusmod tempor incididunt ut labore et dolore magna aliqua. Ut enim ad minim veniam, quis nostrud</p>
<ul class="abs checks" style="left:657px;top:0">
  <li style="top:1832px"><span class="tick"><svg width="9" height="9" viewBox="0 0 10 10"><path d="M2 5l2 2 4-4" stroke="#111" stroke-width="1.6" fill="none"/></svg></span>Professional-grade sharpening methods</li>
  <li style="top:1866px"><span class="tick"><svg width="9" height="9" viewBox="0 0 10 10"><path d="M2 5l2 2 4-4" stroke="#111" stroke-width="1.6" fill="none"/></svg></span>Fast turnaround times</li>
  <li style="top:1899px"><span class="tick"><svg width="9" height="9" viewBox="0 0 10 10"><path d="M2 5l2 2 4-4" stroke="#111" stroke-width="1.6" fill="none"/></svg></span>Affordable pricing</li>
  <li style="top:1933px"><span class="tick"><svg width="9" height="9" viewBox="0 0 10 10"><path d="M2 5l2 2 4-4" stroke="#111" stroke-width="1.6" fill="none"/></svg></span>Local small business service</li>
  <li style="top:1967px"><span class="tick"><svg width="9" height="9" viewBox="0 0 10 10"><path d="M2 5l2 2 4-4" stroke="#111" stroke-width="1.6" fill="none"/></svg></span>Precision edge restoration</li>
</ul>

<section class="abs pricing"></section>
<h2 class="abs h2 center" style="top:2258px">Simple, transparent pricing</h2>
<div class="abs rule" style="left:559px;top:2314px"></div>
<p class="abs lead" style="left:310px;top:2348px;width:580px">Lorem ipsum dolor sit amet, consectetur adipiscing elit, sed do eiusmod tempor incididunt ut labore et dolore magna aliqua. Ut enim ad mini</p>

<div class="abs price-card" style="left:64px">
  <div class="price-photo" role="img" aria-label="Chef's knife with a black handle" style="background:linear-gradient(135deg,#ffffff,#e6e6e6)"></div>
  <div class="price-bar"><span>Kitchen knives</span><span>$ 20.00</span></div>
</div>
<div class="abs price-card" style="left:335px">
  <div class="price-photo" role="img" aria-label="Scissors with red handles" style="background:linear-gradient(135deg,#ffffff,#e8e3e3)"></div>
  <div class="price-bar"><span>Scissors</span><span>$ 20.00</span></div>
</div>
<div class="abs price-card" style="left:607px">
  <div class="price-photo" role="img" aria-label="Set of garden pruners and trowels with orange handles" style="background:linear-gradient(135deg,#ffffff,#e6e4e1)"></div>
  <div class="price-bar"><span>Garden tools</span><span>$ 20.00</span></div>
</div>
<div class="abs price-card" style="left:878px">
  <div class="price-photo" role="img" aria-label="Katana blade with a wrapped handle" style="background:linear-gradient(135deg,#ffffff,#e4e4e4)"></div>
  <div class="price-bar"><span>Blades</span><span>$ 20.00</span></div>
</div>

<section class="abs how"></section>
<h2 class="abs h2 center" style="top:2967px">How it works</h2>
<div class="abs rule" style="left:559px;top:3023px"></div>
<p class="abs lead" style="left:240px;top:3065px;width:720px">Lorem ipsum dolor sit amet, consectetur adipiscing elit, sed do eiusmod tempor incididunt ut labore et dolore magna aliqua. Ut enim ad mini</p>

<svg class="abs" style="left:0;top:3160px" width="1200" height="160" fill="none" stroke="#fff" stroke-width="2" stroke-dasharray="8 6">
  <path d="M340 120 C 420 150 480 140 530 120"/>
  <path d="M668 60 C 740 30 810 40 865 60"/>
</svg>
<div class="abs round step-icon" style="left:201px;top:3179px">
  <svg width="70" height="70" viewBox="0 0 70 70" fill="none" stroke="#111" stroke-width="2"><rect x="10" y="18" width="38" height="32" rx="3"/><path d="M10 26h38M24 18v12h10V18"/><path d="M52 38c-5 0-8 4-8 8 0 6 8 14 8 14s8-8 8-14c0-4-3-8-8-8z"/><circle cx="52" cy="46" r="3"/></svg>
</div>
<div class="abs round step-icon" style="left:530px;top:3179px">
  <svg width="70" height="70" viewBox="0 0 70 70" fill="none" stroke="#111" stroke-width="2"><circle cx="38" cy="40" r="18"/><circle cx="38" cy="40" r="5"/><path d="M12 46 40 14l4 4-28 32z"/><path d="M50 14l4-4M56 20l4-2"/></svg>
</div>
<div class="abs round step-icon" style="left:863px;top:3179px">
  <svg width="70" height="70" viewBox="0 0 70 70" fill="none" stroke="#111" stroke-width="2"><path d="M12 56l8-22 10 4 10-4 10 4 8 18-12-4-8 4-10-4z"/><path d="M35 8c-6 0-10 5-10 10 0 8 10 18 10 18s10-10 10-18c0-5-4-10-10-10z"/><circle cx="35" cy="18" r="4"/></svg>
</div>
<div class="abs step-name" style="left:120px;top:3355px">Drop off your tools</div>
<div class="abs step-name" style="left:449px;top:3355px">Professional sharpening<br>process</div>
<div class="abs step-name" style="left:782px;top:3355px">Pick up razor-sharp results</div>

<section class="abs connect"></section>
<h2 class="abs h2" style="left:124px;top:3643px">Connect with us</h2>
<div class="abs rule" style="left:124px;top:3697px"></div>
<div class="abs round c-icon" style="left:122px;top:3737px">
  <svg width="20" height="20" viewBox="0 0 24 24"><path fill="#111" d="M12 2a7 7 0 0 0-7 7c0 5 7 13 7 13s7-8 7-13a7 7 0 0 0-7-7zm0 9.5A2.5 2.5 0 1 1 12 6.5a2.5 2.5 0 0 1 0 5z"/></svg>
</div>
<div class="abs c-title" style="left:191px;top:3737px">Bolt Plum</div>
<p class="abs c-text" style="left:191px;top:3774px">18392 Calloway Lane<br>Marlow Springs, CA 91307</p>
<div class="abs round c-icon" style="left:122px;top:3857px">
  <svg width="20" height="20" viewBox="0 0 24 24"><path fill="#111" d="M6.6 10.8a15 15 0 0 0 6.6 6.6l2.2-2.2c.3-.3.7-.4 1-.2 1.1.4 2.3.6 3.6.6.6 0 1 .4 1 1V20c0 .6-.4 1-1 1A17 17 0 0 1 3 4c0-.6.4-1 1-1h3.5c.6 0 1 .4 1 1 0 1.3.2 2.5.6 3.6.1.3 0 .7-.2 1z"/></svg>
</div>
<div class="abs c-title" style="left:191px;top:3857px">Call us now</div>
<p class="abs c-text" style="left:191px;top:3894px">661-555-0172</p>
<div class="abs btn btn-white" style="left:131px;top:3958px;width:178px;height:43px">Get direction</div>
<div class="abs map" role="img" aria-label="Map showing the shop location and surrounding towns"></div>

<section class="abs cta"></section>
<h2 class="abs cta-title center" style="top:4226px">Ready to restore your edge?</h2>
<div class="abs rule" style="left:559px;top:4283px;background:var(--ink)"></div>
<p class="abs cta-text center" style="top:4320px">Bring your tools back to peak performance today.</p>
<div class="abs btn btn-dark" style="left:534px;top:4375px;width:134px;height:39px">Call now</div>

<nav class="footer-nav">
  <a href="#" style="left:364px">Home</a>
  <a href="#" style="left:432px">Services</a>
  <a href="#" style="left:527px">Pricing</a>
  <a href="#" style="left:614px">How it works</a>
  <a href="#" style="left:747px">Contact us</a>
</nav>
<div class="abs brand" style="left:160px;top:4626px"><span class="brand-mark"></span>BOLT PLUM</div>
<p class="abs copy" style="left:161px;top:4684px">Bolt Plum © 2026. All Rights Reserved</p>
<div class="abs round c-icon" style="left:494px;top:4617px">
  <svg width="20" height="20" viewBox="0 0 24 24"><path fill="#111" d="M12 2a7 7 0 0 0-7 7c0 5 7 13 7 13s7-8 7-13a7 7 0 0 0-7-7zm0 9.5A2.5 2.5 0 1 1 12 6.5a2.5 2.5 0 0 1 0 5z"/></svg>
</div>
<div class="abs c-title" style="left:565px;top:4618px">Bolt Plum</div>
<p class="abs c-text" style="left:565px;top:4656px">18392 Calloway Lane<br>Marlow Springs, CA 91307</p>
<div class="abs round c-icon" style="left:846px;top:4617px">
  <svg width="20" height="20" viewBox="0 0 24 24"><path fill="#111" d="M6.6 10.8a15 15 0 0 0 6.6 6.6l2.2-2.2c.3-.3.7-.4 1-.2 1.1.4 2.3.6 3.6.6.6 0 1 .4 1 1V20c0 .6-.4 1-1 1A17 17 0 0 1 3 4c0-.6.4-1 1-1h3.5c.6 0 1 .4 1 1 0 1.3.2 2.5.6 3.6.1.3 0 .7-.2 1z"/></svg>
</div>
<div class="abs c-title" style="left:915px;top:4618px">Call us now</div>
<p class="abs c-text" style="left:915px;top:4656px">661-555-0172</p>

</body>
</html>
```